Spirituality Supplement Company Needs A Product Label Design

We are a spirituality company, blog, supplement, company. Our initial product is a supplement that helps with creativity, resilence, and immunity.

We would like to see designs that incorporate a cool design for our product label. The final design should communicate mystical, informed, reassuring, knowledgeable, guiding, wisdom. We attached a picture of our logo. However, I am looking for a more simple and more eye catching design for the logo. You can use the logo attached as a template or to get ideas. We want you to modify our logo for this product design for our supplement to make it more simple and eye catching. Our tagline is Free Your Mind

The ingredients we will have on our supplement is Lions Mane, Reishi, and Turkey Tail mushrooms.

it will be 2 and a half inches width and 10 inches at length. the product label will be on a dark amber glass bottle. (see attached image on post)

Target Market(s)

The driving desires for our consumers are inner power and understanding. Our consumers have a thirst for knowledge and self transformation. Our consumers are into philosophy. Our goal is to show them the path to wisdom.

Our customers primary drives are wisdom, intelligence, expertise, information, influence, transformation, knowledge, vision, belief, and discovery.

Their primary fears are consequences, stagnation, ignorance, doubt, uncertainty, insanity, powerlessness, misinformation, inaccuracy.

Requirements
Must have
• Ingredients labeled. Lions Mane, Reishi, and Turkey Tail Mushroom.
Nice to have
• To show the supplement is promoting Creativity, Resilence, and Immunity.

mind, heart, and body.

I prefer more boldness than elegance. More Playful than serious, more modern than traditional, more personable than professional, more masculine than feminine , more colorful than conservative.

Our mission statement which is, Our mission is to help self actualizing individuals to discover themselves.

It would also be cool if it can look psychedelic.

have the organic, non gmo, 100% natural, vegan, gluten free symbols on product label.

```html
<!DOCTYPE html>
<html lang="en">
<head>
<meta charset="utf-8">
<title>Spirituality Supplement Label</title>
<link href="https://fonts.googleapis.com/css2?family=Montserrat:wght@400;500;700;800&display=swap" rel="stylesheet">
<style>
  :root {
    --gold: #e8c174;
    --ink: #16161c;
    --ink-soft: #22232b;
    --ember: #6e1a12;
    --page: #f1f1f1;
  }
  html, body {
    margin: 0;
    width: 1200px;
    height: 1075px;
    overflow: hidden;
    background: var(--page);
    font-family: "Montserrat", Arial, sans-serif;
  }
  .label {
    position: absolute;
    left: 20px;
    top: 393px;
    width: 1160px;
    height: 289px;
    background: var(--gold);
    box-shadow: 0 6px 14px rgba(0,0,0,0.25);
  }
  .label__panel {
    position: absolute;
    left: 12px;
    top: 12px;
    right: 12px;
    bottom: 10px;
    background: var(--ink);
    overflow: hidden;
    color: var(--gold);
  }
  .label__pattern {
    position: absolute;
    inset: 0;
    background:
      radial-gradient(circle at 27% 55%, rgba(80,82,96,0.28), transparent 22%),
      radial-gradient(circle at 77% 55%, rgba(80,82,96,0.28), transparent 22%),
      linear-gradient(90deg, var(--ink) 0%, var(--ink-soft) 50%, var(--ink) 100%);
  }
  .mission {
    position: absolute;
    left: 30px;
    top: 26px;
    font-size: 15.5px;
    line-height: 19.5px;
    font-weight: 500;
    white-space: nowrap;
  }
  .mission p { margin: 0 0 17px; }
  .badges {
    position: absolute;
    left: 30px;
    top: 180px;
    display: flex;
    gap: 12px;
  }
  .badge {
    width: 51px;
    text-align: center;
    font-size: 7px;
    font-weight: 700;
    white-space: nowrap;
  }
  .badge__mark {
    width: 50px;
    height: 50px;
    border: 2.5px solid var(--gold);
    border-radius: 50%;
    box-sizing: border-box;
    margin: 0 auto 7px;
  }
  .brand {
    position: absolute;
    left: 510px;
    top: 10px;
    width: 134px;
    height: 134px;
    border-radius: 50%;
    background: var(--ember);
    display: flex;
    align-items: center;
    justify-content: center;
  }
  .brand__name {
    font-size: 15px;
    font-weight: 700;
    letter-spacing: 2px;
    color: var(--gold);
    white-space: nowrap;
  }
  .title {
    position: absolute;
    left: 377px;
    top: 153px;
    width: 400px;
    text-align: center;
    margin: 0;
    line-height: 1;
  }
  .title__main {
    display: block;
    font-size: 37px;
    font-weight: 800;
    letter-spacing: 0.5px;
  }
  .title__sub {
    display: block;
    font-size: 29px;
    font-weight: 500;
    letter-spacing: 0.8px;
    margin-top: 2px;
  }
  .facts {
    position: absolute;
    left: 825px;
    top: 26px;
    font-size: 12.5px;
    line-height: 15.5px;
    font-weight: 500;
    white-space: nowrap;
  }
  .facts p { margin: 0 0 18px; }
  .code-box {
    position: absolute;
    left: 919px;
    top: 177px;
    width: 193px;
    height: 59px;
    background: var(--gold);
  }
</style>
</head>
<body>
  <div class="label">
    <div class="label__panel">
      <div class="label__pattern" role="img" aria-label="Faint sacred geometry pattern of triangles and circles"></div>

      <div class="mission">
        <p>Our mission statement which is,<br>Our mission is to help self<br>actualizing individuals to discover<br>themselves.</p>
        <p>It would also be cool if it can look<br>psychedelic.</p>
      </div>

      <div class="badges">
        <div class="badge"><div class="badge__mark"></div>GLUTEN FREE</div>
        <div class="badge"><div class="badge__mark"></div>GMO FREE</div>
        <div class="badge"><div class="badge__mark"></div>ORGANIC</div>
        <div class="badge"><div class="badge__mark"></div></div>
      </div>

      <div class="brand">
        <div class="brand__name">LUMEN VALE</div>
      </div>

      <h1 class="title">
        <span class="title__main">SPIRITUALITY</span>
        <span class="title__sub">SUPPLEMENT</span>
      </h1>

      <div class="facts">
        <p>Ingredients.<br>Lions Mane, Reishi, and Turkey Tail Mushroom.</p>
        <p>Lorem ipsum dolor sit amet, consectetuer<br>adipiscing elit, sed diam nonummy nibh<br>euismod tincidunt ut laoreet dolore magna<br>aliquam</p>
      </div>

      <div class="code-box"></div>
    </div>
  </div>
</body>
</html>
```